Postcard Project

I need a postcard designed 6X9 in size printed full color
Will need in the end a high resolution print ready file with crop marks
See instructions in word doc

```html
<!DOCTYPE html>
<html lang="en">
<head>
<meta charset="utf-8">
<title>Drinkware Promotion Postcard</title>
<link href="https://fonts.googleapis.com/css2?family=Bebas+Neue&family=Anton&family=Tinos&family=Roboto:wght@400&display=swap" rel="stylesheet">
<style>
  :root {
    --promo-red: #ff0000;
    --ink: #000000;
    --paper: #ffffff;
    --backdrop: #e4e4e4;
    --enamel: #f1f1f1;
    --brick: #c8352e;
    --charcoal: #2a2a2a;
    --stoneware: #b5a285;
    --cup-red: #d60000;
    --bottle-blue: #1f66d1;
    --cork: #a26a42;
  }
  * { margin: 0; padding: 0; box-sizing: border-box; }
  html, body { width: 1200px; height: 872px; overflow: hidden; background: var(--backdrop); }
  .postcard {
    position: absolute; left: 18px; top: 48px;
    width: 1164px; height: 776px;
    background: var(--paper); overflow: hidden;
  }
  .headline {
    position: absolute; left: 0; width: 100%;
    text-align: center; color: var(--promo-red);
    font-family: "Bebas Neue", sans-serif; font-size: 56px; line-height: 1;
  }
  .headline--offer { top: 30px; }
  .headline--code { top: 100px; }
  .sku-list {
    position: absolute; left: 71px; top: 184px;
    list-style: none; font-family: "Tinos", serif;
    font-size: 25px; line-height: 32px; color: var(--ink);
    white-space: nowrap;
  }
  .referral-box {
    position: absolute; left: 586px; top: 171px;
    width: 578px; height: 212px; background: var(--promo-red);
    padding: 12px 0 0 20px;
    font-family: "Anton", sans-serif; font-size: 30px; line-height: 36px;
    color: var(--paper); white-space: nowrap;
  }
  .first-offer {
    position: absolute; left: 585px; top: 390px;
    font-family: "Anton", sans-serif; font-size: 28px; line-height: 33px;
    color: var(--ink); white-space: nowrap;
  }
  .first-offer .code { color: var(--promo-red); }
  .product { position: absolute; }
  .product--tumbler { left: 71px; top: 516px; width: 77px; height: 158px; border-radius: 8px 8px 18px 18px; background: linear-gradient(90deg, #a9acae, #eceeef 45%, #b9bcbe); }
  .product--camp-mug { left: 170px; top: 530px; width: 143px; height: 135px; border-radius: 6px 6px 14px 14px; background: linear-gradient(90deg, #dcdcdc, var(--enamel) 50%, #d8d8d8); }
  .product--bottle { left: 362px; top: 524px; width: 37px; height: 140px; border-radius: 10px 10px 6px 6px; background: linear-gradient(90deg, #9e2520, var(--brick) 50%, #a52a24); }
  .product--black-mug { left: 439px; top: 540px; width: 130px; height: 113px; border-radius: 10px 10px 30px 30px; background: linear-gradient(90deg, #1c1c1c, var(--charcoal) 50%, #1c1c1c); }
  .product--stone-mug { left: 588px; top: 519px; width: 141px; height: 158px; border-radius: 10px 10px 22px 22px; background: linear-gradient(180deg, var(--enamel) 0 64%, var(--stoneware) 64%); }
  .product--stadium-cup { left: 745px; top: 522px; width: 103px; height: 150px; border-radius: 6px 6px 16px 16px; background: linear-gradient(90deg, #b30000, var(--cup-red) 50%, #b30000); }
  .product--sport-bottle { left: 890px; top: 518px; width: 50px; height: 155px; border-radius: 14px 14px 8px 8px; background: linear-gradient(90deg, #1650a8, var(--bottle-blue) 50%, #1650a8); }
  .product--travel-tumbler { left: 1003px; top: 516px; width: 73px; height: 161px; border-radius: 10px 10px 14px 14px; background: linear-gradient(180deg, #2a2a2a 0 10%, var(--enamel) 10% 88%, var(--cork) 88%); }
  .footer-band { position: absolute; left: 0; top: 723px; width: 1164px; height: 53px; }
  .address {
    position: absolute; left: 68px; top: 723px;
    font-family: "Roboto", sans-serif; font-size: 44px; line-height: 52px;
    color: var(--paper); white-space: nowrap;
  }
  .footer-tag {
    position: absolute; left: 600px; width: 564px; top: 723px;
    text-align: center; font-family: "Anton", sans-serif;
    font-size: 36px; line-height: 52px; color: var(--paper); white-space: nowrap;
  }
</style>
</head>
<body>
<main class="postcard">
  <h1 class="headline headline--offer">DRINKWARE - $50 OFF ON YOUR DRINKWARE ORDER OVER $500</h1>
  <h2 class="headline headline--code">PROMO CODE DRINK GOOD TILL 9/30/25</h2>

  <ul class="sku-list">
    <li>7401-12SL_B_BACK Black</li>
    <li>7402-38WH_A_BACK Full Color</li>
    <li>7402-51RD_B_BACK White</li>
    <li>7405-17BK_B_FR_3041 White</li>
    <li>7405-62WH_B_FR_8120 Full</li>
    <li>DW-3307RD_B_FR Black</li>
    <li>DW-3842RBL_B__5216White</li>
    <li>DW-3915WH_B_FR_2684Black</li>
  </ul>

  <section class="referral-box">
    <p>REFER a Friend GIVE $100, GET $100</p>
    <p>Give your friends $100 off their first purchase</p>
    <p>(over $500) and receive a $100 discount</p>
    <p>on any order (over $500).</p>
    <p>Promo Code REFER</p>
  </section>

  <section class="first-offer">
    <p>$150 off your first department purchase of $500</p>
    <p class="code">Promo Code FIRST150</p>
    <p>Promotions cannot be combined</p>
  </section>

  <div class="product product--tumbler" role="img" aria-label="Silver twisted stainless tumbler with clear lid"></div>
  <div class="product product--camp-mug" role="img" aria-label="White enamel camp mug with lid"></div>
  <div class="product product--bottle" role="img" aria-label="Red insulated water bottle with loop cap"></div>
  <div class="product product--black-mug" role="img" aria-label="Black ceramic mug"></div>
  <div class="product product--stone-mug" role="img" aria-label="White ceramic mug with speckled stoneware base"></div>
  <div class="product product--stadium-cup" role="img" aria-label="Red plastic stadium cup"></div>
  <div class="product product--sport-bottle" role="img" aria-label="Blue plastic sport squeeze bottle"></div>
  <div class="product product--travel-tumbler" role="img" aria-label="White travel tumbler with black lid and cork base"></div>

  <svg class="footer-band" viewBox="0 0 1164 53" aria-hidden="true">
    <polygon points="0,0 563,0 592,53 0,53" fill="var(--ink)"/>
    <polygon points="572,0 1164,0 1164,53 600,53" fill="var(--promo-red)"/>
    <path d="M28 12a11 11 0 0 0-11 11c0 8 11 20 11 20s11-12 11-20a11 11 0 0 0-11-11zm0 15a4 4 0 1 1 0-8 4 4 0 0 1 0 8z" fill="var(--paper)"/>
  </svg>
  <p class="address">Address line here</p>
  <p class="footer-tag">1st purchase &amp; referral</p>
</main>
</body>
</html>
```